Website/Logo Design

We need a logo and website design for an opinion mining startup called VantroLux. Our technology mines the web to automatically discover what people are saying about brands, products, etc. The project we are fielding here is for our informational, public-facing website. In its initial incarnation, it will simply be a vehicle for marketing materials and information on our company and its offerings, but it should be flexible enough to expand as more content/functionality is added.

Some designs we like are:
http://www.brivel-nodo.com
http://www.tarnwisp.com
http://www.kvh.com
http://www.zellmorit.com
http://quontavel.com
http://marbiquex.com
http://www.vadup.com
Updates

All, please try to shy away from using a photo of a person as the focal point of the design.  Our company is more technological than social.

Target Market(s)

Primarily businesses interested in sentiment analysis (typically companies involved in advertising, market research, PR, etc.)

Industry/Entity Type

It Company

Requirements
Must have
• We are looking for a clean, modern, and professional design. This includes a logo, homepage, and internal page if it will differ from the homepage.
Nice to have
• It would be excellent if you could provide an HTML mockup if your design is chosen.
Should not have
• Flash, excessive bells and whistles

```html
<!DOCTYPE html>
<html lang="en">
<head>
<meta charset="utf-8">
<title>VantroLux</title>
<link href="https://fonts.googleapis.com/css2?family=Didact+Gothic&family=Nunito:wght@600;700&family=Alegreya+Sans:wght@500&family=Noto+Sans:wght@400&display=swap" rel="stylesheet">
<style>
:root{
  --brand-blue:#1a5fa8;
  --brand-green:#8cc63f;
  --band-top:#2a8ccb;
  --band-bottom:#0c4d88;
  --heading:#2a8ac6;
  --link:#1a78b8;
  --body:#333;
  --page:#f4f4f4;
  --panel:#ffffff;
  --btn-top:#3a9ad6;
  --btn-bottom:#0b4f8a;
  --rule:#cfcfcf;
}
*{margin:0;padding:0;box-sizing:border-box}
html,body{width:1200px;height:977px;overflow:hidden;background:var(--page)}
body{position:relative;font-family:"Noto Sans",sans-serif;color:var(--body)}
.site-header{position:absolute;left:0;top:0;width:1200px;height:121px;background:#fafafa}
.brand{position:absolute;left:122px;top:38px;display:flex;align-items:center;gap:12px}
.brand-mark{width:34px;height:34px;border-radius:50%;background:var(--brand-blue)}
.brand-name{font-family:"Nunito",sans-serif;font-weight:700;font-size:40px;color:var(--brand-blue);letter-spacing:-.5px}
.call{position:absolute;right:122px;top:54px;font-family:"Didact Gothic",sans-serif;font-size:19px;color:var(--brand-blue)}
.call small{font-size:14px}
.main-nav{position:absolute;right:118px;top:94px;display:flex;font-family:"Didact Gothic",sans-serif;font-size:12px;color:#333}
.main-nav a{padding:0 22px;border-left:1px solid #999;line-height:16px;color:inherit;text-decoration:none}
.main-nav a:first-child{border:none}
.main-nav a:last-child{padding-right:0}
.hero{position:absolute;left:0;top:121px;width:1200px;height:242px;background:linear-gradient(var(--band-top),var(--band-bottom));box-shadow:0 8px 14px rgba(0,0,0,.18)}
.hero-text{position:absolute;left:122px;top:88px;font-family:"Nunito",sans-serif;font-weight:700;font-size:20.5px;line-height:24px;color:#fff}
.hero-art{position:absolute;left:648px;top:8px;width:430px;height:232px;border-radius:50%;background:radial-gradient(circle at 50% 45%,#9fd1f6 0,#3d8fdc 35%,rgba(30,110,200,.2) 65%,transparent 72%)}
.panel{position:absolute;background:var(--panel);box-shadow:0 0 4px rgba(0,0,0,.12)}
.btn{display:block;border-radius:7px;background:linear-gradient(var(--btn-top),var(--btn-bottom));color:#fff;font-family:"Alegreya Sans",sans-serif;font-weight:500;text-align:center;box-shadow:0 2px 2px rgba(0,0,0,.25)}
.panel-title{position:absolute;left:11px;width:220px;height:32px;line-height:32px;font-size:18px}
.copy{font-size:10.4px;line-height:13px;letter-spacing:.3px}
.copy p{margin-bottom:13px}
.copy .lead{color:var(--link)}
.copy .more{color:var(--link);display:block;margin-top:-13px}
.search-field{position:absolute;left:11px;top:51px;width:173px;height:27px;border:2px solid #ccc;background:#fff}
.search-go{position:absolute;left:189px;top:51px;width:44px;height:27px;border-radius:4px;background:var(--brand-green);color:#fff;font-family:"Alegreya Sans",sans-serif;font-size:18px;line-height:27px;text-align:center}
.divider{border:none;border-top:1px solid var(--rule);margin:16px 0 28px}
.section-title{font-family:"Nunito",sans-serif;font-weight:700;color:var(--heading);font-size:23px;position:absolute}
.team-photo{position:absolute;left:674px;top:451px;width:152px;height:133px;background:linear-gradient(#e8ecef,#b9c2cc)}
.demo{position:absolute;left:841px;top:404px;width:239px;height:104px;background:var(--brand-green)}
.demo .btn{position:absolute;left:36px;width:180px;height:32px;line-height:32px;font-size:18px}
.social{position:absolute;left:870px;top:580px;display:flex;gap:18px}
.social span{width:37px;height:37px;border-radius:5px;background:var(--link)}
.footer{position:absolute;left:114px;top:912px;width:974px;height:48px;background:linear-gradient(#f8f8f8,#e6e6e6);box-shadow:0 4px 8px rgba(0,0,0,.12);font-size:9.5px;letter-spacing:.4px;line-height:48px}
.footer .l{position:absolute;left:8px}
.footer .c{position:absolute;left:381px}
.footer .r{position:absolute;right:10px}
</style>
</head>
<body>
<header class="site-header">
  <div class="brand"><span class="brand-name">VantroLux</span><span class="brand-mark"></span></div>
  <div class="call"><small>Call:</small> +123 (0) 456 781 920</div>
  <nav class="main-nav"><a>HOME</a><a>ABOUT US</a><a>SERVICES</a><a>OUR BLOGS</a><a>CONTACT US</a></nav>
</header>

<section class="hero">
  <p class="hero-text">Our technology mines the web to<br>automatically discover what people<br>are saying about brands, products, etc</p>
  <div class="hero-art" role="img" aria-label="Illustration of a globe and computer monitor with signal waves"></div>
</section>

<aside class="panel" style="left:122px;top:404px;width:238px;height:104px">
  <div class="btn panel-title" style="top:4px">VantroLux Search</div>
  <div class="search-field"></div>
  <div class="search-go">GO</div>
</aside>

<aside class="panel" style="left:122px;top:520px;width:238px;height:388px">
  <div class="btn panel-title" style="top:3px">VantroLux in the News</div>
  <div class="copy" style="position:absolute;left:17px;top:51px;width:212px">
    <p><span class="lead">Lorem Ipsum is simply</span> dummy text of the printing and typesetting industry. LoremIpsum has been the industry's standarddummy text ever since the 1500s,</p>
    <p>&nbsp;when an unknown printer took a galley of type and scrambled it to make a type specimen book.</p>
    <a class="more">get more detail&gt;&gt;</a>
    <hr class="divider">
    <p><span class="lead">Lorem Ipsum is simply</span> dummy text of the printing and typesetting industry. LoremIpsum has been the industry's standarddummy text ever since the 1500s,</p>
    <p>&nbsp;when an unknown printer took a galley of type and scrambled it to make a type specimen book.</p>
    <a class="more">get more detail&gt;&gt;</a>
  </div>
</aside>

<main>
  <h1 class="section-title" style="left:380px;top:406px">Introducing VantroLux Community</h1>
  <div class="team-photo" role="img" aria-label="Photo of a business team"></div>
  <div class="copy" style="position:absolute;left:379px;top:461px;width:290px">
    <p><span class="lead">Lorem Ipsum is simply</span> dummy text of the printing and typesetting industry. LoremIpsum has been the industry's standarddummy text ever since the 1500s,</p>
    <p>when an unknown printer took a galley of type and scrambled it to make a type specimen book.ummy text of the printing and typesetting industry.</p>
  </div>
  <div class="copy" style="position:absolute;left:379px;top:590px;width:450px">
    <p><span class="lead">Lorem Ipsum is simply</span> dummy text of the printing and typesetting industry. LoremIpsum has been the industry's standarddummy text ever since the 1500s,</p>
    <p>when an unknown printer took a galley of type and scrambled it to make a type specimen book.ummy text of the printing and typesetting industry.</p>
  </div>
  <h2 class="section-title" style="left:378px;top:719px">Recent Blog Post</h2>
  <div class="copy" style="position:absolute;left:379px;top:756px;width:460px">
    <p><span class="lead">Lorem Ipsum is simply</span> dummy text of the printing and typesetting industry. LoremIpsum has been the industry's standarddummy text ever since the 1500s,</p>
    <p>&nbsp;when an unknown printer took a galley of type and scrambled it to make a type specimen book.ummy text of the printing and typesetting industry.</p>
    <p>&nbsp;LoremIpsum has been the industry's stanardummy text ever since the 1500s, when an unknown rinter took a galley of type and scrambled it to make a pe specimen book.</p>
  </div>
</main>

<aside class="demo">
  <div class="btn" style="top:15px">REQUEST A DEMO</div>
  <div class="btn" style="top:59px">CONTACT US</div>
</aside>

<aside class="panel" style="left:841px;top:520px;width:239px;height:105px">
  <div class="btn panel-title" style="left:13px;top:4px">Follow VantroLux</div>
</aside>
<div class="social" role="img" aria-label="Social network links"><span></span><span></span><span></span><span></span></div>

<aside class="panel" style="left:841px;top:638px;width:239px;height:270px">
  <div class="btn panel-title" style="top:4px">VantroLux Anouncements</div>
  <div class="copy" style="position:absolute;left:16px;top:52px;width:215px">
    <p><span class="lead">Lorem Ipsum is simply</span> dummy text of the printing and typesetting industry. LoremIpsum has been the industry's standarddummy text ever since the 1500s,</p>
    <p>when an unknown printer took a galley of type and scrambled it to make a type specimen book.</p>
    <p>&nbsp;when an unknown printer took a galley of type and scrambled it to make a type specimen book.</p>
    <a class="more">get more detail&gt;&gt;</a>
  </div>
</aside>

<footer class="footer">
  <span class="l">Questions? Call Us at +345 (0) 209 847 316</span>
  <span class="c">Privacy Policy &nbsp; | &nbsp; Contact Us &nbsp; | &nbsp; Site Map</span>
  <span class="r">Questions? Call Us at +345 (0) 209 847 316</span>
</footer>
</body>
</html>
```